Veltrane Hand Sanitiser Spray Product Range for International Markets

Veltrane is a new Healthcare business launching a full product range of Anti-bacterial Hand Sanitiser Spray bottles in various sizes. We have a new logo which we believe differentiates us from the competition: Veltrane - Care That Goes Further
The Product Range will comprise two distinct product solution types:
- Anti-bacterial Hand Sanitisers - Alcohol based
- Anti-bacterial Hand Sanitisers - Sensitive Non Alcohol based
Bottle sizes will comprise a range containing:
100ml, 250ml, 500ml, 1ltr, 5ltr, 10ltr
Some bottles will have Pump Sprays
The Product labelling will be attractive front packaging label combined with strong product attributes and usage indicator cues.
As a Healthcare brand our logo design is light Green. We believe that this should be combined with blues and greens balanced to create contrast and strong stand-out on-shelf.
A review of competitor brands will show some similar colour cues, however as a Healthcare brand, the colour cues Green and White are synonymous with the sector. Many existing brands are very pragmatic in their label design. i.e. #it does what is says on the tin approach#. Our brand will need strong stand-out and strong aesthetic appeal too, since it will often be left in public view and around the home and office and therefore should look as attractive as possible. There will be other brand variants in the future and thought should be given to this too - with use of colour cues.
For Competitor indicators check-out the brands on Brisklot - Pine Hollow, Dermavell and others....Thank-you!

Target Market(s)

First: Female 25 - 65
Second: Male 25 - 65

Contact Information for Business Card

Garth L. Dunmore
CEO
Veltrane Healthcare Worldwide
'Care That Goes Further'
www.VeltraneHealthcare.example
E. gldunmore@veltranehealthcare.example
T. +44 7700 900318
T. +44 118 496072

Font styles to use
Sans Serif

Colors
34a7d7
33b8a4
add136
fbee3e
b768aa

```html
<!DOCTYPE html>
<html lang="en">
<head>
<meta charset="utf-8">
<title>Veltrane Anti-Bacterial Hand Sanitiser Label</title>
<link href="https://fonts.googleapis.com/css2?family=Oswald:wght@500;600&family=Open+Sans:wght@700&display=swap" rel="stylesheet">
<style>
  :root {
    --backdrop: #e9e9e9;
    --brand-green: #2aa83a;
    --banner-dark: #1a8c26;
    --banner-light: #66d670;
    --label-white: #ffffff;
  }
  * { margin: 0; padding: 0; box-sizing: border-box; }
  html, body {
    width: 1200px;
    height: 930px;
    overflow: hidden;
    background: var(--backdrop);
  }
  .label {
    width: 1200px;
    height: 930px;
    display: flex;
    flex-direction: column;
    align-items: center;
  }
  .brand-name {
    margin-top: 118px;
    font-family: "Oswald", sans-serif;
    font-weight: 500;
    font-size: 72px;
    line-height: 1;
    color: var(--brand-green);
  }
  .product-banner {
    margin-top: 92px;
    width: 680px;
    height: 250px;
    border-radius: 44px;
    background: linear-gradient(90deg, var(--banner-dark), var(--banner-light));
    display: flex;
    justify-content: center;
    align-items: center;
  }
  .product-name {
    font-family: "Oswald", sans-serif;
    font-weight: 500;
    color: var(--label-white);
    font-size: 96px;
    line-height: 0.92;
    text-align: center;
    letter-spacing: 0.5px;
  }
  .strapline {
    margin-top: 22px;
    font-family: "Oswald", sans-serif;
    font-weight: 500;
    font-size: 54px;
    color: var(--brand-green);
  }
  .product-facts {
    margin-top: 90px;
    text-align: center;
    font-family: "Oswald", sans-serif;
    font-weight: 600;
    color: var(--brand-green);
    font-size: 32px;
    line-height: 1.55;
  }
  .website {
    margin-top: 6px;
    font-family: "Open Sans", sans-serif;
    font-weight: 700;
    font-size: 28px;
    color: var(--brand-green);
  }
</style>
</head>
<body>
  <main class="label">
    <p class="brand-name">Veltrane</p>

    <div class="product-banner">
      <h1 class="product-name">ANTI-BACTERIAL<br>HAND SANITISER</h1>
    </div>

    <p class="strapline">Care That Goes Further</p>

    <div class="product-facts">
      <p>75 % ALCOHOL</p>
      <p>16,9 FL / 500 ML</p>
    </div>

    <p class="website">www.VeltraneHealthcare.example</p>
  </main>
</body>
</html>
```